Trifold for International Business Consulting firm

I have created a trifold piece (attached) that includes all the necessary information in a Word template; however, I need a professional that can make it look "current, international and modern". Our website, brenvaleadvisory.com, should give an idea as to the style and color template we like.

```html
<!DOCTYPE html>
<html lang="en">
<head>
<meta charset="utf-8">
<title>Brenvale Advisory – Trifold</title>
<link rel="stylesheet" href="https://fonts.googleapis.com/css2?family=Mukta:wght@400;700;800&display=swap">
<style>
  :root{
    --green:#a3c83c;
    --green-deep:#8cb92a;
    --green-light:#c9df7a;
    --green-pale:#dcebb0;
    --ink:#3b3b3b;
    --white:#ffffff;
    --photo-dark-a:#2a3a55;
    --photo-dark-b:#8d9aaa;
    --photo-light-a:#e9ecef;
    --photo-light-b:#b9c0c7;
    --photo-warm-a:#f2f2f0;
    --photo-warm-b:#c8b8a6;
  }
  *{box-sizing:border-box;margin:0;padding:0}
  html,body{width:1200px;height:849px;overflow:hidden;background:#fff}
  body{font-family:"Mukta",Arial,sans-serif;color:var(--ink)}
  .trifold{position:relative;width:1200px;height:849px;overflow:hidden;background:var(--white)}
  .panel{position:absolute;top:0;width:400px;height:605px;overflow:hidden}
  .panel--left{left:0;background:var(--white)}
  .panel--middle{left:400px;background:var(--green)}
  .panel--right{left:800px;background:var(--white)}
  .decor{position:absolute;top:0;left:0;width:400px;height:200px}
  .panel-body{position:absolute;font-size:13px;line-height:19px;text-align:justify}
  .panel--left .panel-body{left:37px;top:32px;width:340px}
  .panel--middle .panel-body{left:34px;top:32px;width:332px;color:var(--white)}
  .panel--right .panel-body{left:34px;top:56px;width:340px}
  h2{font-weight:800;text-transform:uppercase;color:var(--green-deep);font-size:17px;line-height:22px;margin-bottom:12px;text-align:left}
  .panel--middle h2{color:var(--white);font-size:19px;line-height:23px}
  p{margin-bottom:9px}
  .gap{margin-top:18px}
  .question-list p{text-align:left}
  strong{font-weight:800}
  .headquarters{text-align:center;margin-top:18px}
  .headquarters h3{font-weight:800;font-size:14px;line-height:19px;margin-bottom:3px}
  .headquarters p{text-align:center;margin:0;font-size:13.5px;line-height:20px}
  .photo{position:absolute;top:605px;width:400px;height:222px}
  .photo--strategy{left:0;background:linear-gradient(120deg,var(--photo-dark-b),var(--photo-dark-a) 55%,#c9d0d8)}
  .photo--meeting{left:400px;background:linear-gradient(160deg,var(--photo-light-a),var(--photo-light-b))}
  .photo--team{left:800px;background:linear-gradient(150deg,var(--photo-warm-a),var(--photo-warm-b))}
  .base-band{position:absolute;left:0;top:827px;width:1200px;height:22px;background:var(--green)}
</style>
</head>
<body>
<div class="trifold">

  <section class="panel panel--left">
    <svg class="decor" viewBox="0 0 400 200" aria-hidden="true">
      <polygon points="315,0 400,0 400,85" fill="var(--green-pale)"/>
      <polygon points="345,40 375,10 400,35 370,65" fill="var(--green-light)" opacity=".8"/>
    </svg>
    <div class="panel-body">
      <h2>Should we expand?</h2>
      <p>It depends: Brenvale Advisory can assist you in an initial analysis to see if your company is prepared financially to expand and if the current infrastructure is adequate for international operations. We look at human resources, technology, operations, systems, processes and do a complete SWOT analysis of your current operation.</p>
      <div class="question-list">
        <p>1.Have you maximized your current opportunities? Is your company mature for this endeavor?</p>
        <p>2.Have you discussed with all invested parties and taken all feedback into consideration?</p>
        <p>3.What are your short, mid and long term goals for growth?</p>
      </div>
      <p>If you are not ready for international expansion today, we will design the path to help you get there.</p>
      <h2 class="gap">How do we expand?</h2>
      <p>One of three ways:</p>
      <div class="question-list">
        <p>1.Green pasture-organic growth. Evolve your current business internationally, or create a new business from scratch</p>
        <p>2.Joint Venture (JV) - partner with another entity in country of expansion</p>
        <p>3.Merger or Acquisition (M&amp;A) - merge or acquire a new entity in country of expansion</p>
      </div>
    </div>
  </section>

  <section class="panel panel--middle">
    <svg class="decor" viewBox="0 0 400 200" aria-hidden="true">
      <polygon points="0,0 70,0 0,70" fill="var(--green-light)" opacity=".55"/>
      <polygon points="330,0 400,0 400,70" fill="var(--green-light)" opacity=".45"/>
    </svg>
    <div class="panel-body">
      <h2>Which expansion opportunity is best for my company?</h2>
      <p>Each opportunity has its own pros and cons for growth which can be largely dependent on the country of expansion and your budget. Some countries are business friendly for new business creation and growth while others are more optimal for international businesses to join, merge or acquire established companies in country.</p>
      <p>To determine the best way forward, it is good practice to seek counsel on your different options. Our networks specialize in all categories needed for international expansion, and our consultants coordinate with each specialist to work in unison for your best interest.</p>
      <h2 class="gap">Working with specialists</h2>
      <p>We have spent years developing relationships with accounting, legal and financial specialists necessary for international growth. We have business associates located on both sides of the border, positioned for cost and time efficiencies and with the expertise you need to succeed in your growth plans.</p>
      <p>Instead of parading individual groups of specialists in front of you, each with its own sales pitch and service offerings, we introduce and manage the entire relationship and service. With a single point of contact and negotiated rates for your benefit, we keep your costs at an optimal level.</p>
    </div>
  </section>

  <section class="panel panel--right">
    <svg class="decor" viewBox="0 0 400 200" aria-hidden="true">
      <polygon points="0,0 90,0 0,90" fill="var(--green-pale)" opacity=".8"/>
      <polygon points="330,0 400,0 400,70" fill="var(--green-light)" opacity=".8"/>
    </svg>
    <div class="panel-body">
      <h2>Cultural managment</h2>
      <p>In addition to international business consulting services, we have expertise in the cultural intricacies of international business and offer Meridian Culture training.</p>
      <p>We have more than 20 years of experience consulting and training multinational companies, small and mid size companies as well as individuals looking to improve their international business skills.</p>
      <p>There is significant evidence that cross-cultural training and knowledge lead to more successful international business relationships and they are key to success for mergers and acquisitions as well as joint ventures.</p>
      <p>“Your Success Drives our Success.” It is our goal to be a long term partner in your international growth strategies and development. <strong>Contact us today to get started.</strong></p>
      <p><strong>Offices in Houston, New York City, San Antonio, Monterrey, Guadalajara and Mexico City.</strong></p>
      <div class="headquarters">
        <h3>Headquarters</h3>
        <p>Brenvale Advisory<br>418 Calder Ridge Blvd, Suite 120, Austin, TX 78701<br>Phone (512) 555-0187 | info@brenvaleadvisory.com<br>www.brenvaleadvisory.com</p>
      </div>
    </div>
  </section>

  <div class="photo photo--strategy" role="img" aria-label="Photo of a businessman in a suit sketching circles and arrows of a growth strategy"></div>
  <div class="photo photo--meeting" role="img" aria-label="Overhead photo of a business team meeting around a white table"></div>
  <div class="photo photo--team" role="img" aria-label="Photo of a cheerful business team giving a group high five"></div>
  <div class="base-band"></div>
</div>
</body>
</html>
```